Design Insurance Salesman Business Cards

****FIINAL FILES MUST BE SUBMITTED AS PSD LAYERED FILES WITH EDITABLE TEXT (300dpi, CMYK color)****

The main design element of this business card should be an umbrella that connects to the Y in the first name (Beatrix). There should be rain drops above the umbrella but not below it. The Umbrella connected to the name will serve as the logo. (see attachment "sample [login to view URL]" for an example. The umbrella can be angled if you want)

The card should be navy blue and gold. The umbrella should be gold OR red if you can make red look good on a mostly blue and gold design.

Here is the rest of the information for your mock ups:

FRONT
Beatrix Whitcombe (Y' connected to Umbrella)
Financial Professional l Coach
412-555-7263
Info@[login to view URL]
[login to view URL]

BACK (*this list is long and should be split into two columns)
•Senior Market Advisor
•Living benefits
•Tax-Free Retirement
•Mortgage Protection
•College Planning
•Business Preservation
•1 on 1 Coaching
•Group Coaching
•Workshop Facilitator
•Professional Speaker

```html
<!DOCTYPE html>
<html lang="en">
<head>
<meta charset="utf-8">
<title>Beatrix Whitcombe – Business Cards</title>
<link href="https://fonts.googleapis.com/css2?family=Roboto:wght@400;500;700&display=swap" rel="stylesheet">
<style>
  :root {
    --backdrop: #c6c6c6;
    --navy: #10152f;
    --gold: #f3c348;
    --white: #f2f2f2;
    --umbrella-red: #d8222a;
    --umbrella-red-deep: #a8141c;
  }
  * { box-sizing: border-box; margin: 0; padding: 0; }
  html, body {
    width: 1200px;
    height: 1200px;
    overflow: hidden;
    background: var(--backdrop);
    font-family: "Roboto", Arial, sans-serif;
  }
  .canvas { position: relative; width: 1200px; height: 1200px; }
  .card {
    position: absolute;
    left: 221px;
    width: 757px;
    height: 433px;
    background: var(--navy);
    border-radius: 19px;
  }
  .card--back { top: 101px; }
  .card--front { top: 607px; }

  /* Back: services list */
  .services {
    position: absolute;
    top: 130px;
    list-style: none;
    color: var(--gold);
    font-size: 23px;
    line-height: 35px;
  }
  .services--left { left: 83px; }
  .services--right { left: 428px; }

  /* Front: identity */
  .name-bar {
    position: absolute;
    left: 0; top: 177px;
    width: 4px; height: 56px;
    background: var(--gold);
  }
  .holder-name {
    position: absolute;
    left: 25px; top: 170px;
    color: var(--gold);
    font-weight: 700;
    font-size: 30px;
  }
  .holder-title {
    position: absolute;
    left: 25px; top: 210px;
    color: var(--white);
    font-size: 17px;
  }
  .rule {
    position: absolute;
    left: 24px; top: 267px;
    width: 95px; height: 3px;
    background: var(--gold);
  }
  .contacts {
    position: absolute;
    left: 24px; top: 305px;
    list-style: none;
    color: var(--white);
    font-size: 21px;
    line-height: 34px;
  }
  .contacts li { display: flex; align-items: center; gap: 12px; }
  .contacts svg { width: 20px; height: 20px; flex: none; }

  /* Front: umbrella artwork area */
  .umbrella-art {
    position: absolute;
    left: 366px; top: 50px;
    width: 332px; height: 222px;
    border-radius: 6px;
    background: radial-gradient(ellipse at 50% 35%, var(--umbrella-red) 0%, var(--umbrella-red-deep) 70%);
  }

  .wordmark {
    position: absolute;
    right: 26px; top: 276px;
    text-align: center;
    color: var(--gold);
    font-weight: 400;
    font-size: 50px;
    line-height: 62px;
  }
</style>
</head>
<body>
<main class="canvas">

  <section class="card card--back" aria-label="Card back: services">
    <ul class="services services--left">
      <li>•Senior Market Advisor</li>
      <li>•Living benefits</li>
      <li>•Tax-Free Retirement</li>
      <li>•Mortgage Protection</li>
      <li>•College Planning</li>
    </ul>
    <ul class="services services--right">
      <li>•Business Preservation</li>
      <li>•1 on 1 Coaching</li>
      <li>•Group Coaching</li>
      <li>•Workshop Facilitator</li>
      <li>•Professional Speaker</li>
    </ul>
  </section>

  <section class="card card--front" aria-label="Card front: contact details">
    <span class="name-bar"></span>
    <h1 class="holder-name">Beatrix Whitcombe</h1>
    <p class="holder-title">Financial Professional l Coach</p>
    <span class="rule"></span>
    <ul class="contacts">
      <li>
        <svg viewBox="0 0 24 24" fill="none" stroke="var(--gold)" stroke-width="2" stroke-linecap="round" stroke-linejoin="round" aria-hidden="true">
          <path d="M5 3h4l2 5-2.5 1.5a11 11 0 0 0 6 6L16 13l5 2v4a2 2 0 0 1-2 2A17 17 0 0 1 3 5a2 2 0 0 1 2-2z"/>
        </svg>
        412-555-7263
      </li>
      <li>
        <svg viewBox="0 0 24 24" aria-hidden="true">
          <rect x="2" y="5" width="20" height="14" fill="var(--gold)"/>
          <path d="M2 5l10 8 10-8" fill="none" stroke="var(--navy)" stroke-width="1.8"/>
        </svg>
        Info@beatrixwhitcombe.com
      </li>
      <li>
        <svg viewBox="0 0 24 24" fill="none" stroke="var(--gold)" stroke-width="1.8" aria-hidden="true">
          <circle cx="12" cy="12" r="9.5"/>
          <ellipse cx="12" cy="12" rx="4" ry="9.5"/>
          <path d="M2.5 12h19M4 7h16M4 17h16"/>
        </svg>
        www.beatrixwhitcombe.com
      </li>
    </ul>
    <div class="umbrella-art" role="img" aria-label="Photograph of an open red umbrella with a gold handle"></div>
    <p class="wordmark">Beatrix<br>Whitcombe</p>
  </section>

</main>
</body>
</html>
```